New Personal Training Studio needs A6 size, full colour, double sided flyer designed.

We need a flyer designed for our New Personal Training Studio located in Northvale NSW 2037 Australia. We are an innovative NEW form of fitness, a true one stop health shop. We offer personal/corporate training and group training both indoors and outdoors, we also have our own mini fresh whole food market in our studio supplying ethically-rasied, free range, hormone free meats, pasture fed eggs, organic dairy and chemical free and pestercide free fruit and vegetables. We have add on services we offer such as health and fitness assessments and lifestlye coaching, plus the studio has shower/toilet facilities. Plus all our classes have exercises options for first timers to the advanced. We do whole body function fitness.

Our main clientel are females ages 20 to 45years old who work full time.

Our busness Name is Brightpath Fitness, we already have a business logo and website which you can refer to www.brightpathfitness-demo.com

We would like to see designs that incorporate colours from our website and logo with a similar approach, plus for the flyer to target those interested in getting in shape for their new years resolution in 2012. We would need the flyer completed ideally by 20/12/11 so we can send them off for printing and be ready for janurary 2012.

The final design should focus on our group training classes as that is our biggest part of the business, but also talk about all our other services. It should include our current promotion for our group training 'Special Introductory Offer $5 per class for your first 5 classes", plus show a min map of our location, website, phone number and a focus on the new year, new you , new studio.

I have a previous home desinged flyer which you can use as a starting point if need be.
Updates

Just an additional note, I will need it to have a 5mm bleed all around it on the front and back.

Hey Designer,

I have just got the correct files you need for the logo in ai and other formats, please see the new 3 uploads.

Reason: To allow for more designer to submit work I have extended the deadline by 3 days.

Hi designers, I haveĀ 2 updates regarding this job.

1. I have a photo shoot today and will have lots of new photos of the studio so you can add them to the flyer. We only want to use actual photos of our location and our clients in the flyer.

2. I will extend the due date to early Jan 2012 as we are wanting to really get the first flyer perfect

 

Reason: The dead line has been extended as we really want to see more designs coming through and with the holiday season at our door steps this is just not happenning. This extension is absolutly final as we will need to send off the flyers for printing the following day.

Designers, I have just added $150 for a second place position for our flyer design comp, so keep up the great work and keep the designs coming in : )

Target Market(s)

Females, aged 20 to 45 working class who want to get in shape.

Industry/Entity Type

Training

Requirements
Must have
• Must be full colour, double sided, A6 high resolution, incorporate exisitng logo and use colours from website.
Should not have
• Please do not use the old map in our old flyer, we want a new map. This is a must

```html
<!DOCTYPE html>
<html lang="en">
<head>
<meta charset="utf-8">
<title>Brightpath Fitness – New Year Flyer</title>
<link rel="stylesheet" href="https://fonts.googleapis.com/css2?family=Baloo+2:wght@600;700;800&display=swap">
<style>
  :root {
    --sky: #2f8fd8;
    --sky-deep: #0f4f9a;
    --sky-light: #8fd0f5;
    --lime: #c9f126;
    --lime-soft: #e6fbb0;
    --leaf: #5ca523;
    --leaf-deep: #2f6d0f;
    --panel: #6cb52c;
    --white: #ffffff;
    --ink: #1c1c1c;
    --violet: #6b6cf2;
    --new-blue: #2f9ff0;
    --shadow: rgba(0,0,0,.8);
  }
  * { box-sizing: border-box; margin: 0; padding: 0; }
  html, body { width: 1200px; height: 846px; overflow: hidden; background: var(--white); }
  .flyer { position: relative; width: 1200px; height: 846px; overflow: hidden;
    font-family: "Baloo 2", sans-serif; font-weight: 600; color: var(--white); }
  .side { position: absolute; top: 0; height: 846px; overflow: hidden;
    background: linear-gradient(180deg, #ffffff 22%, var(--lime-soft) 50%, #ffffff 78%); }
  .side--front { left: 0; width: 606px; }
  .side--back { left: 610px; width: 590px; }
  .fold { position: absolute; left: 606px; top: 0; width: 4px; height: 846px; background: var(--leaf); opacity: .6; }
  .photo { position: absolute; left: 0; width: 100%; }
  .photo--hero { top: 0; height: 230px;
    background: linear-gradient(160deg, var(--sky-light), var(--sky) 50%, var(--sky-deep)); }
  .photo--studio { top: 0; height: 185px;
    background: linear-gradient(200deg, var(--sky-light), var(--sky) 55%, var(--sky-deep)); }
  .photo--grass { bottom: 0; height: 95px;
    background: linear-gradient(180deg, rgba(140,210,40,0) 0%, #7cc22a 40%, #3c7f12 100%); }
  .swoosh { position: absolute; left: 0; top: 150px; width: 100%; height: 160px; }
  .shadowed { text-shadow: 0 0 2px var(--shadow), 1px 1px 0 var(--shadow), -1px -1px 0 var(--shadow), 2px 2px 4px var(--shadow); }

  .brand { position: absolute; left: 110px; top: 72px; display: flex; align-items: center; gap: 14px; }
  .brand__dot { width: 34px; height: 34px; border-radius: 50%; background: var(--lime); }
  .brand__name { font-size: 50px; line-height: .95; font-weight: 700; color: var(--white); }

  .tagline { position: absolute; left: 55px; top: 245px; width: 520px; transform: rotate(-11deg);
    font-weight: 800; font-size: 22px; text-align: center; line-height: 1.05; }
  .tagline strong { color: var(--lime); font-size: 40px; }

  .newyear { position: absolute; left: 60px; top: 350px; font-weight: 800; }
  .newyear__year { font-size: 54px; color: var(--leaf); line-height: 1; }
  .newyear__you { font-size: 40px; color: var(--lime); margin: 8px 0 0 92px; line-height: 1; }
  .newyear__you em { font-style: normal; color: var(--new-blue); }

  .offer { position: absolute; left: 0; top: 484px; width: 606px; text-align: center; }
  .offer__title { font-weight: 800; font-size: 29px; letter-spacing: 1px; }
  .offer__deal { display: flex; justify-content: center; align-items: center; gap: 12px; margin-top: -8px; }
  .offer__price { font-weight: 800; font-size: 82px; color: var(--violet); line-height: 1; }
  .offer__terms { font-size: 22px; text-align: left; line-height: 1; font-weight: 700; }

  .card { position: absolute; background: linear-gradient(180deg, #7fc13a, var(--panel) 60%, #4f9a1c);
    border-radius: 14px; text-align: center; color: var(--white); box-shadow: 0 2px 6px rgba(0,0,0,.3); font-weight: 700; }
  .card--benefits { left: 65px; top: 625px; width: 462px; height: 155px; padding: 10px 8px; font-size: 17.5px; line-height: 1.45; }
  .card--features { left: 45px; top: 187px; width: 505px; height: 215px; padding: 8px 10px; font-size: 16px; line-height: 1.25; }
  .card--features p { margin-bottom: 11px; }

  .headline { position: absolute; left: 90px; top: 50px; width: 420px; text-align: center;
    font-weight: 800; line-height: 1.02; color: var(--lime); font-size: 29px; }
  .headline b { color: var(--white); font-size: 36px; }

  .services { position: absolute; left: 55px; top: 410px; width: 290px; text-align: center;
    font-size: 30px; line-height: 1.17; font-weight: 700; }
  .map { position: absolute; left: 372px; top: 410px; width: 176px; height: 146px;
    border: 3px solid var(--white); box-shadow: 0 2px 5px rgba(0,0,0,.4);
    background: linear-gradient(135deg, #e8e6e1, #d6e8c4 60%, #b9d6ef); }
  .address { position: absolute; right: 47px; top: 570px; text-align: right; font-style: normal;
    font-family: Arial, sans-serif; font-size: 14px; line-height: 1.12; color: var(--ink); }

  .contact { position: absolute; left: 27px; top: 538px; }
  .contact__title { font-weight: 800; font-size: 36px; color: var(--lime); line-height: 1.1; }
  .contact__phone { font-size: 34px; line-height: 1.1; font-weight: 700; letter-spacing: 1px; }
  .contact__line { font-size: 22px; line-height: 1.5; font-weight: 700; }

  .reviews { position: absolute; right: 142px; top: 740px; text-align: right; font-size: 12.5px; line-height: 1.35; font-weight: 700; }
  .reviews a { color: #4fb0ff; text-decoration: none; }
  .badge { position: absolute; left: 455px; top: 727px; width: 75px; height: 80px; border-radius: 6px;
    background: var(--white); box-shadow: 0 1px 4px rgba(0,0,0,.5); }
</style>
</head>
<body>
<main class="flyer">

  <section class="side side--front">
    <div class="photo photo--hero" role="img" aria-label="Studio photos of clients doing chin-ups and ball exercises with a trainer"></div>
    <svg class="swoosh" viewBox="0 0 606 160" preserveAspectRatio="none" aria-hidden="true">
      <path d="M0 70 C150 20 350 120 606 40 L606 160 L0 160 Z" fill="#ffffff"/>
      <path d="M0 95 C180 50 360 130 606 70" stroke="#9fdc3a" stroke-width="10" fill="none" opacity=".7"/>
    </svg>
    <div class="brand">
      <span class="brand__dot"></span>
      <span class="brand__name">Brightpath<br>Fitness</span>
    </div>
    <p class="tagline shadowed">Improve Your <strong>Health, Fitness,</strong> and <strong>Vitality</strong> with us!</p>
    <div class="newyear shadowed">
      <p class="newyear__year">2012 is here!</p>
      <p class="newyear__you">Time for a <em>NEW</em> you!</p>
    </div>
    <div class="offer">
      <p class="offer__title shadowed">SPECIAL INTRODUCTORY OFFER!</p>
      <div class="offer__deal">
        <span class="offer__price shadowed">$5</span>
        <span class="offer__terms shadowed">per class for your<br>first 5 classes</span>
      </div>
    </div>
    <div class="card card--benefits shadowed">
      <p>Lose that unwanted bodyfat!</p>
      <p>Tone those troublesome areas!</p>
      <p>Gain strenth, flexibility, and cardio fitness!</p>
      <p>Attain that sexy summer body you desire!</p>
      <p>Improve your energy and vitality!</p>
    </div>
    <div class="photo photo--grass" role="img" aria-label="Green grass with gym dumbbells"></div>
  </section>

  <div class="fold" aria-hidden="true"></div>

  <section class="side side--back">
    <div class="photo photo--studio" role="img" aria-label="Studio photos of women training with exercise balls"></div>
    <h2 class="headline shadowed"><b>OVER 20 CLASSES</b><br>TO CHOOSE FROM<br>in our <b>NEW STUDIO!</b></h2>
    <div class="card card--features shadowed">
      <p>Fun, varied, and exciting training programs!</p>
      <p>Expert trainers to guide, support, and motivate you!</p>
      <p>Close to Market Lane Shops, Harbourside, and CBD!</p>
      <p>Excercise options for ALL fitness levels<br>from first timers to the athletic!</p>
      <p>Over 20 classes to choose from, ranging<br>from morning, evening, and weekend classes!</p>
    </div>
    <p class="services shadowed">Group Training<br>Personal Training<br>Asessments</p>
    <div class="map" role="img" aria-label="Street map showing the studio location"></div>
    <address class="address">Brightpath Fitness Studio<br>Studio 9<br>12 Parkline Road<br>Northvale 2999</address>
    <div class="contact">
      <p class="contact__title shadowed">Contact Us!</p>
      <p class="contact__phone shadowed">0400 123 987</p>
      <p class="contact__line shadowed">hello@brightpathfitness-demo.com</p>
      <p class="contact__line shadowed">http://www.brightpathfitness-demo.com/</p>
      <p class="contact__line shadowed">https://social.brightpathfitness-demo.com</p>
    </div>
    <div class="photo photo--grass" role="img" aria-label="Green grass with gym dumbbells"></div>
    <p class="reviews shadowed">Don't just take our word for it. See for yourself<br>what people are saying about Brightpath Fitness!<br>Read our reviews on <a href="#">www.localvoice-demo.com.au</a></p>
    <div class="badge" aria-hidden="true"></div>
  </section>

</main>
</body>
</html>
```